Business Card Design Project

We need a business card designed for a new Luxury Custom Homebuilding company based in Arizona. We previous were called "Belcrest Estates" but want to start using "Belcrest Custom Homes" We want the message to communicate high end, luxury and cutting-edge. We like the blue, white and black color scheme.
Belcrest Custom Homes
Marcus T. Halloway
Chief Executive Officer
Office: 480-555-0142
Mobile: 480-555-0178
email: marc@belcrestcustom-example.com
web adress: www.BelcrestCustom-example.com
Updates
We have made a change to our website address and email address based on recieving feedback from a nmber of individuals. The feedback was web address and email address was to long. Therefore we have made a change. The new web adress and email adress are the following.
www.BelcrestCustom-example.com
marc@belcrestcustom-example.com
Also I decided against using in yellow. I like the colors blue,black, white and maybe gray.
Target Market(s)
Our target market is the wealthy individuals looking for a luxury high-end custom home.
Industry/Entity Type
Business
Look and feel

```html
<!DOCTYPE html>
<html lang="en">
<head>
<meta charset="utf-8">
<title>Belcrest Custom Homes – Business Card</title>
<link rel="stylesheet" href="https://fonts.googleapis.com/css2?family=Source+Sans+3:wght@400;600;700;800&display=swap">
<style>
  :root {
    --charcoal: #353535;
    --white: #ffffff;
    --blue: #5b9bd5;
    --blue-light: #a9c8ea;
    --ink: #3a3a3a;
    --page: #ffffff;
    --shadow: rgba(0, 0, 0, 0.35);
  }
  * { margin: 0; padding: 0; box-sizing: border-box; }
  html, body {
    width: 1200px;
    height: 1000px;
    overflow: hidden;
    background: var(--page);
    font-family: "Source Sans 3", "Myriad Pro", sans-serif;
  }
  .card {
    position: absolute;
    left: 285px;
    width: 658px;
    height: 375px;
    box-shadow: 3px 4px 6px var(--shadow);
    overflow: hidden;
  }
  .card--front { top: 94px; background: var(--charcoal); }
  .card--back { top: 533px; background: var(--white); }

  .card__art { position: absolute; inset: 0; width: 100%; height: 100%; }

  .wordmark {
    position: absolute;
    color: var(--white);
    font-weight: 800;
    text-align: right;
    line-height: 1;
  }
  .wordmark__name { display: block; font-size: 74px; letter-spacing: -2px; }
  .wordmark__line { display: block; font-size: 27px; letter-spacing: 0.5px; margin-top: 4px; }

  .card--front .wordmark { right: 36px; top: 196px; }
  .card--back .wordmark { left: 34px; top: 136px; }

  .front-web {
    position: absolute;
    right: 34px;
    top: 320px;
    color: var(--white);
    font-size: 17px;
    letter-spacing: 0.4px;
  }
  .front-web__accent { color: var(--blue); }

  .holder {
    position: absolute;
    right: 41px;
    top: 109px;
    text-align: right;
  }
  .holder__name { color: var(--blue); font-size: 22px; font-weight: 600; line-height: 1.2; }
  .holder__title { color: var(--ink); font-size: 16.5px; margin-top: 2px; }

  .contacts {
    position: absolute;
    right: 41px;
    top: 218px;
    list-style: none;
  }
  .contacts__item {
    display: flex;
    justify-content: flex-end;
    align-items: center;
    gap: 10px;
    height: 22px;
    color: var(--ink);
    font-size: 16px;
  }
  .contacts__icon { width: 16px; height: 16px; flex: none; }
  .contacts__icon * { fill: var(--blue); }
</style>
</head>
<body>

<section class="card card--front" aria-label="Card front">
  <div class="wordmark">
    <span class="wordmark__name">Belcrest</span>
    <span class="wordmark__line">CUSTOM HOMES</span>
  </div>
  <p class="front-web">www.Belcrest<span class="front-web__accent">Custom</span>-example.com</p>
</section>

<section class="card card--back" aria-label="Card back">
  <svg class="card__art" viewBox="0 0 658 375" aria-hidden="true">
    <defs>
      <linearGradient id="swoosh" x1="0" y1="0" x2="0" y2="1">
        <stop offset="0" stop-color="var(--blue-light)"/>
        <stop offset="0.55" stop-color="var(--blue-light)"/>
        <stop offset="1" stop-color="var(--blue)"/>
      </linearGradient>
    </defs>
    <path d="M0 0 H380 Q360 245 226 375 H0 Z" fill="var(--charcoal)"/>
    <path d="M384 0 H390 Q378 252 250 375 H232 Q366 245 384 0 Z" fill="url(#swoosh)"/>
  </svg>

  <div class="wordmark">
    <span class="wordmark__name">Belcrest</span>
    <span class="wordmark__line">CUSTOM HOMES</span>
  </div>

  <div class="holder">
    <p class="holder__name">Marcus T. Halloway</p>
    <p class="holder__title">Chief Executive Officer</p>
  </div>

  <ul class="contacts">
    <li class="contacts__item">480-555-0142
      <svg class="contacts__icon" viewBox="0 0 16 16" aria-label="Office phone"><path d="M1 6 Q8 0 15 6 L13 8 L11 6 V5 H5 V6 L3 8 Z"/><path d="M4 9 H12 L13 14 H3 Z"/></svg>
    </li>
    <li class="contacts__item">480-555-0178
      <svg class="contacts__icon" viewBox="0 0 16 16" aria-label="Mobile phone"><path d="M4 1 H12 V15 H4 Z M5 3 V12 H11 V3 Z"/></svg>
    </li>
    <li class="contacts__item">marc@belcrestcustom-example.com
      <svg class="contacts__icon" viewBox="0 0 16 16" aria-label="Email"><path d="M1 3 H15 L8 9 Z"/><path d="M1 4.5 L8 10.5 L15 4.5 V13 H1 Z"/></svg>
    </li>
    <li class="contacts__item">www.BelcrestCustom-example.com
      <svg class="contacts__icon" viewBox="0 0 16 16" aria-label="Website"><path d="M8 1 A7 7 0 1 0 8.01 1 Z M8 2.3 A5.7 5.7 0 1 1 7.99 2.3 Z"/><path d="M2 7.4 H14 V8.6 H2 Z M7.4 2 H8.6 V14 H7.4 Z"/><path d="M8 2 Q4 8 8 14 Q5.5 8 8 2 Z M8 2 Q12 8 8 14 Q10.5 8 8 2 Z"/></svg>
    </li>
  </ul>
</section>

</body>
</html>
```